Eye catching Bottle label for pink gin targeting women 25+

We need a new label for a re-launch of our shimmering strawberry pink gin liqueur. We would like it to look premium and eye catching on the shelf. We have 2 labels we require, one for 200ml bottle (2x2 inches) and one for 500ml bottle 4x4 inches). Label must state the ml of the bottle abd that it is 18.75%Vol. Also say Shimmering Strawberry Gin Liqueur with the brand name at the top - Marlow Tide. We have a logo but it doesn't need to be used if it doesn't work with the design/colours. The gin is presented in a clear bottle and is pink and sparkly. See uploaded image for reference.

Target Market(s)

Women aged 25-45

Font styles to use
Decorative

Colors
f59296
fbd4d5
eea4c8

Requirements
Must have
• Bottle size - 500ml/200ml
• Must say 18.75% Vol
• Must have brand name - Marlow Tide
• Must have product name - Shimmering Pink Strawberry
• Must say - Gin Liqueur
Nice to have
• Some sort of floral or swirley background detail would be nice
Should not have
• Must not appeal to children

```html
<!DOCTYPE html>
<html lang="en">
<head>
<meta charset="utf-8">
<title>Marlow Tide Gin Liqueur Labels</title>
<link rel="stylesheet" href="https://fonts.googleapis.com/css2?family=Jost:wght@500;600&family=Open+Sans:wght@700&display=swap">
<style>
  :root {
    --page: #ffffff;
    --label-bg: #ebbabc;
    --pattern: #eec8c4;
    --band: #eb5f9f;
    --gin: #e5005b;
    --brand-dark: #4a0c08;
    --white: #ffffff;
    --info: #4a0e0e;
  }
  html, body {
    margin: 0;
    padding: 0;
    width: 848px;
    height: 1200px;
    overflow: hidden;
    background: var(--page);
  }
  .sheet {
    position: relative;
    width: 848px;
    height: 1200px;
  }
  .label {
    position: absolute;
    left: 218px;
    width: 396px;
    height: 396px;
    display: block;
  }
  .label--200 { top: 126px; }
  .label--500 { top: 639px; }
  .label-bg { fill: var(--label-bg); }
  .floral-area { fill: url(#floralTone); }
  .brand-disc { fill: var(--brand-dark); }
  .brand-name {
    font-family: "Jost", sans-serif;
    font-weight: 500;
    font-size: 21px;
    fill: var(--white);
  }
  .product-type {
    font-family: "Jost", sans-serif;
    font-weight: 600;
    fill: var(--gin);
  }
  .product-type--main { font-size: 117px; }
  .product-type--sub { font-size: 34px; }
  .flavour-band { fill: var(--band); }
  .flavour {
    font-family: "Jost", sans-serif;
    font-weight: 600;
    font-size: 29px;
    fill: var(--white);
  }
  .bottle-info {
    font-family: "Open Sans", sans-serif;
    font-weight: 700;
    font-size: 19px;
    fill: var(--info);
  }
</style>
</head>
<body>
<div class="sheet">
  <svg width="0" height="0" style="position:absolute" aria-hidden="true">
    <defs>
      <linearGradient id="floralTone" x1="0" y1="0" x2="1" y2="1">
        <stop offset="0" stop-color="#ecc2c1"/>
        <stop offset="1" stop-color="#ebbabc"/>
      </linearGradient>
    </defs>
  </svg>

  <svg class="label label--200" viewBox="0 0 396 396" role="group" aria-label="200ml bottle label">
    <rect class="label-bg" x="0" y="0" width="396" height="396"/>
    <rect class="floral-area" x="0" y="0" width="396" height="396" role="img" aria-label="Soft cream floral swirl pattern across the label background"/>
    <circle class="brand-disc" cx="198" cy="67" r="60"/>
    <text class="brand-name" x="198" y="62" text-anchor="middle">Marlow</text>
    <text class="brand-name" x="198" y="86" text-anchor="middle">Tide</text>
    <text class="product-type product-type--main" x="107" y="225" textLength="180" lengthAdjust="spacingAndGlyphs">GIN</text>
    <text class="product-type product-type--sub" x="129" y="261" textLength="137" lengthAdjust="spacingAndGlyphs">LIQUEUR</text>
    <rect class="flavour-band" x="0" y="284" width="396" height="70"/>
    <text class="flavour" x="107" y="314" textLength="172" lengthAdjust="spacingAndGlyphs">SHIMMERING</text>
    <text class="flavour" x="74" y="343" textLength="248" lengthAdjust="spacingAndGlyphs">PINK STRAWBERRY</text>
    <text class="bottle-info" x="111" y="383" textLength="169" lengthAdjust="spacingAndGlyphs">200ml |18.75% Vol</text>
  </svg>

  <svg class="label label--500" viewBox="0 0 396 396" role="group" aria-label="500ml bottle label">
    <rect class="label-bg" x="0" y="0" width="396" height="396"/>
    <rect class="floral-area" x="0" y="0" width="396" height="396" role="img" aria-label="Soft cream floral swirl pattern across the label background"/>
    <circle class="brand-disc" cx="198" cy="67" r="60"/>
    <text class="brand-name" x="198" y="62" text-anchor="middle">Marlow</text>
    <text class="brand-name" x="198" y="86" text-anchor="middle">Tide</text>
    <text class="product-type product-type--main" x="107" y="225" textLength="180" lengthAdjust="spacingAndGlyphs">GIN</text>
    <text class="product-type product-type--sub" x="129" y="261" textLength="137" lengthAdjust="spacingAndGlyphs">LIQUEUR</text>
    <rect class="flavour-band" x="0" y="284" width="396" height="70"/>
    <text class="flavour" x="107" y="314" textLength="172" lengthAdjust="spacingAndGlyphs">SHIMMERING</text>
    <text class="flavour" x="74" y="343" textLength="248" lengthAdjust="spacingAndGlyphs">PINK STRAWBERRY</text>
    <text class="bottle-info" x="111" y="383" textLength="169" lengthAdjust="spacingAndGlyphs">500ml |18.75% Vol</text>
  </svg>
</div>
</body>
</html>
```